redesign existing business card

Re design our business cards. We want a modern elegant design, open to ideas front side must contain similar details in a fresh look and style, back side we are open to suggestions. MUST USE COMPANY COLORS, WE WANT BRANDING. Need more ideas see www.duskmoorstoneworks.com - Project must be done in one of adobe products and all files and fonts must be submitted to us. THIS IS A MUST

Target Market(s)

home owners

Industry/Entity Type

Construction Company

Contact Information for Business Card

see existing card file for information

Font styles to use
Sans Serif

Colors
0455a3
3377b5
34a6d7
0592cd
85cae6
ffffff

Requirements
Must have
• company colors, logo, contact info this is all for front side. back side be creative.

```html
<!DOCTYPE html>
<html lang="en">
<head>
<meta charset="utf-8">
<title>Duskmoor Stoneworks — Business Card</title>
<link href="https://fonts.googleapis.com/css2?family=Roboto+Condensed:ital,wght@0,400;0,700;1,400;1,700&display=swap" rel="stylesheet">
<style>
  :root{
    --brand-deep:#0455a3;
    --brand-mid:#3377b5;
    --brand-band:#3d5fae;
    --brand-bright:#34a6d7;
    --brand-sky:#85cae6;
    --white:#ffffff;
    --stage:#eceef1;
    --shadow:rgba(20,30,50,.28);
  }
  *{box-sizing:border-box;margin:0;padding:0}
  html,body{width:1200px;height:1200px;overflow:hidden}
  body{background:var(--stage);font-family:"Roboto Condensed",Arial,sans-serif;position:relative}

  .card{position:absolute;left:260px;width:680px;height:380px;overflow:hidden;background:var(--white);box-shadow:0 14px 24px -10px var(--shadow)}
  .card--front{top:170px}
  .card--back{top:620px}
  .card__bg{position:absolute;inset:0;width:100%;height:100%}

  .brand{position:absolute;display:flex;flex-direction:column;align-items:center;gap:10px}
  .brand__mark{width:44px;height:44px;background:var(--brand-bright)}
  .brand__name{font-weight:700;font-size:24px;letter-spacing:1px;color:var(--brand-deep);text-transform:uppercase;text-align:center;line-height:1.05}
  .card--front .brand{left:50%;top:34px;transform:translateX(-50%)}
  .card--back .brand{left:150px;top:120px;transform:translateX(-50%)}

  .contact{position:absolute;color:var(--white)}
  .contact--person{left:80px;top:246px}
  .contact__name{font-weight:700;font-size:27px;letter-spacing:.5px;text-transform:uppercase;line-height:1}
  .contact__line{font-size:15px;line-height:19px}
  .contact__direct{margin-top:8px;margin-bottom:10px}
  .contact__label{font-weight:700;text-transform:uppercase}
  .divider{position:absolute;left:324px;top:250px;width:2px;height:118px;background:var(--white)}
  .contact--channels{left:350px;top:252px;display:flex;flex-direction:column;gap:11px}
  .channel{display:flex;align-items:center;gap:10px;font-size:15px;line-height:20px}
  .channel svg{width:20px;height:20px;flex:none}

  .paving{position:absolute;left:290px;top:0;width:390px;height:380px;
    background:linear-gradient(160deg,#b8a79c 0%,#a2867c 35%,#8f6f69 60%,#a79a93 100%)}
  .paving__veil{position:absolute;left:340px;top:0;width:250px;height:380px;background:rgba(255,255,255,.35)}
  .services{position:absolute;left:340px;width:250px;text-align:center;color:var(--brand-deep);
    font-style:italic;text-transform:uppercase;font-size:14px;line-height:16px}
  .services--list{top:72px}
  .services--credentials{top:280px;font-weight:700}
</style>
</head>
<body>

<section class="card card--front" aria-label="Business card front">
  <svg class="card__bg" viewBox="0 0 680 380" preserveAspectRatio="none" aria-hidden="true">
    <path d="M0 214 C220 236 480 220 680 70 L680 380 L0 380 Z" fill="var(--brand-sky)"/>
    <path d="M0 220 C230 242 500 236 680 100 L680 380 L0 380 Z" fill="var(--brand-bright)"/>
    <path d="M0 228 C240 248 520 250 680 128 L680 380 L0 380 Z" fill="var(--brand-band)"/>
  </svg>

  <div class="brand">
    <span class="brand__mark"></span>
    <span class="brand__name">Duskmoor<br>Stoneworks</span>
  </div>

  <div class="contact contact--person">
    <p class="contact__name">Marco Teixeira</p>
    <p class="contact__line contact__direct">Direct: (555) 318-204</p>
    <p class="contact__line contact__label">Office – Showroom</p>
    <p class="contact__line">1480 Fenmoor Way Suite 6</p>
    <p class="contact__line">Ashvale, FL 33900</p>
  </div>

  <span class="divider"></span>

  <div class="contact contact--channels">
    <p class="channel">
      <svg viewBox="0 0 24 24"><path fill="#fff" d="M6.6 10.8a15 15 0 0 0 6.6 6.6l2.2-2.2c.3-.3.7-.4 1-.2 1.1.4 2.3.6 3.6.6.6 0 1 .4 1 1V20c0 .6-.4 1-1 1A17 17 0 0 1 3 4c0-.6.4-1 1-1h3.5c.6 0 1 .4 1 1 0 1.3.2 2.5.6 3.6.1.3 0 .7-.2 1z"/></svg>
      O: (555) 270-4816
    </p>
    <p class="channel">
      <svg viewBox="0 0 24 24"><path fill="#fff" d="M6.6 10.8a15 15 0 0 0 6.6 6.6l2.2-2.2c.3-.3.7-.4 1-.2 1.1.4 2.3.6 3.6.6.6 0 1 .4 1 1V20c0 .6-.4 1-1 1A17 17 0 0 1 3 4c0-.6.4-1 1-1h3.5c.6 0 1 .4 1 1 0 1.3.2 2.5.6 3.6.1.3 0 .7-.2 1z"/></svg>
      F: (555) 270-4817
    </p>
    <p class="channel">
      <svg viewBox="0 0 24 24"><rect x="3" y="6" width="18" height="13" rx="1.5" fill="#fff"/><path d="M4 7l8 6 8-6" fill="none" stroke="var(--brand-band)" stroke-width="1.6"/></svg>
      Marco@DuskmoorStoneworks.com
    </p>
    <p class="channel">
      <svg viewBox="0 0 24 24" fill="none" stroke="#fff" stroke-width="1.6"><circle cx="12" cy="12" r="9"/><ellipse cx="12" cy="12" rx="4" ry="9"/><path d="M3 12h18M5 7h14M5 17h14"/></svg>
      www.duskmoorstoneworks.com
    </p>
  </div>
</section>

<section class="card card--back" aria-label="Business card back">
  <svg class="card__bg" viewBox="0 0 680 380" preserveAspectRatio="none" aria-hidden="true">
    <rect width="680" height="380" fill="var(--brand-band)"/>
    <path d="M0 110 C100 78 220 70 300 72 L300 320 C200 318 90 310 0 300 Z" fill="var(--brand-bright)"/>
    <path d="M0 122 C100 90 220 84 300 86 L300 308 C200 306 90 300 0 290 Z" fill="var(--white)"/>
  </svg>

  <div class="paving" role="img" aria-label="Photograph of a fan-pattern paver driveway in red, tan and grey stones"></div>
  <div class="paving__veil"></div>

  <div class="brand">
    <span class="brand__mark"></span>
    <span class="brand__name">Duskmoor<br>Stoneworks</span>
  </div>

  <p class="services services--list">
    Driveway<br>
    Pool Renovation<br>
    Custom Out-Door Kitchen<br>
    Retaining Wall<br>
    Paver Restoration<br>
    H.O.A Projects<br>
    Patios &amp; Much More
  </p>

  <p class="services services--credentials">
    Family Owned &amp; Operated<br>
    License &amp; Insured<br>
    LIC 22-S18 4471-K CTY RLN U-30514<br>
    County MC#058213
  </p>
</section>

</body>
</html>
```